HarmoNest Ensemble Jubilee
Date: Sunday Oct 2, 2022
When: 2-4 p.m.
Location: Brindle9 Alehouse
413 Marlowe Ct #200, Sacramento, CA 95821
Tickets: www.Tixolvo.com
General seating: $15 for adults and $10 for students

```html
<!DOCTYPE html>
<html lang="en">
<head>
<meta charset="utf-8">
<title>HarmoNest Ensemble Jubilee</title>
<link rel="stylesheet" href="https://fonts.googleapis.com/css2?family=Russo+One&family=Great+Vibes&family=Oswald:wght@500&family=Roboto:wght@400;500&display=swap">
<style>
  :root {
    --backdrop: #d9d9db;
    --poster-black: #07040a;
    --plum-deep: #2a0c2e;
    --plum: #6b1f62;
    --magenta: #b0338f;
    --cream: #f6e6cf;
    --gold: #d9b36c;
    --gold-soft: #e8cf9a;
    --white: #ffffff;
  }
  * { margin: 0; padding: 0; box-sizing: border-box; }
  html, body { width: 1200px; height: 1200px; overflow: hidden; background: var(--backdrop); }
  .poster {
    position: absolute; left: 136px; top: 0;
    width: 927px; height: 1200px;
    background: var(--poster-black);
    overflow: hidden;
    font-family: "Roboto", sans-serif;
    color: var(--white);
  }
  .stage-art {
    position: absolute; left: 0; top: 0; width: 100%; height: 800px;
    background:
      radial-gradient(circle at 20% 14%, rgba(255,230,255,0.55) 0, rgba(255,200,255,0) 9%),
      radial-gradient(circle at 60% 62%, rgba(214,64,150,0.75) 0, rgba(120,30,100,0.35) 22%, rgba(0,0,0,0) 42%),
      radial-gradient(circle at 22% 35%, rgba(170,80,170,0.7) 0, rgba(90,30,90,0.4) 24%, rgba(0,0,0,0) 45%),
      radial-gradient(ellipse at 70% 18%, var(--plum) 0, var(--plum-deep) 45%, var(--poster-black) 85%);
  }
  .stage-art::after {
    content: ""; position: absolute; left: 0; right: 0; bottom: 0; height: 220px;
    background: linear-gradient(to bottom, rgba(7,4,10,0), var(--poster-black));
  }
  .title { position: absolute; right: 80px; top: 105px; text-align: right; }
  .title-main {
    font-family: "Russo One", sans-serif; font-size: 118px; line-height: 1;
    color: var(--cream); text-shadow: 0 4px 0 #7a5a3a, 0 8px 18px rgba(0,0,0,0.6);
  }
  .title-sub {
    font-family: "Russo One", sans-serif; font-size: 74px; line-height: 1;
    margin-top: 24px; margin-right: 4px;
    color: var(--cream); text-shadow: 0 3px 0 #7a5a3a, 0 6px 14px rgba(0,0,0,0.6);
  }
  .title-script {
    font-family: "Great Vibes", cursive; font-size: 130px; line-height: 1;
    margin-top: -4px; margin-right: 60px;
    color: var(--gold-soft); text-shadow: 0 3px 0 #5a3e26, 0 6px 14px rgba(0,0,0,0.7);
  }
  .when { position: absolute; left: 0; right: 0; top: 730px; text-align: center; }
  .when-day { font-weight: 500; font-size: 28px; letter-spacing: 10px; margin-left: 10px; }
  .when-date {
    font-family: "Oswald", sans-serif; font-weight: 500; font-size: 96px; line-height: 1.05;
    color: var(--cream); margin-top: 4px;
  }
  .when-time {
    display: flex; justify-content: center; align-items: center; gap: 22px;
    font-weight: 500; font-size: 27px; letter-spacing: 9px; margin-top: 4px; margin-left: -70px;
  }
  .details { position: absolute; left: 70px; right: 90px; top: 1000px; display: flex; justify-content: space-between; align-items: center; }
  .venue { display: flex; align-items: center; gap: 22px; font-size: 20px; line-height: 1.3; }
  .pricing { display: flex; align-items: center; gap: 14px; font-size: 20px; }
  .pricing-label { font-size: 17px; line-height: 1.3; }
  .pricing-brace { font-size: 52px; font-weight: 400; line-height: 1; color: var(--white); transform: scaleX(0.5); }
  .pricing-values { line-height: 1.3; }
  .website {
    position: absolute; left: 0; right: 0; top: 1112px; text-align: center;
    font-size: 38px; font-weight: 500; letter-spacing: 4px; color: var(--gold-soft);
  }
  .website-rule {
    position: absolute; left: 250px; right: 250px; top: 1166px; height: 1px;
    background: linear-gradient(to right, rgba(217,179,108,0), var(--gold), rgba(217,179,108,0));
  }
</style>
</head>
<body>
<main class="poster">
  <div class="stage-art" role="img" aria-label="Vintage chrome microphone with glowing purple speakers and a cheering concert crowd in silhouette"></div>

  <h1 class="title">
    <div class="title-main">HarmoNest</div>
    <div class="title-sub">ENSEMBLE</div>
    <div class="title-script">Jubilee</div>
  </h1>

  <section class="when">
    <div class="when-day">SUNDAY</div>
    <div class="when-date">Oct 2, 2022</div>
    <div class="when-time">
      <svg width="38" height="38" viewBox="0 0 38 38" aria-hidden="true">
        <circle cx="19" cy="19" r="17" fill="none" stroke="var(--gold)" stroke-width="3"/>
        <circle cx="19" cy="19" r="11" fill="var(--gold)"/>
        <path d="M19 12 V19 H25" stroke="var(--poster-black)" stroke-width="2.5" fill="none" stroke-linecap="round"/>
      </svg>
      <span>2-4 P.M.</span>
    </div>
  </section>

  <section class="details">
    <div class="venue">
      <svg width="40" height="58" viewBox="0 0 40 58" aria-hidden="true">
        <path d="M20 2 C9 2 2 10 2 20 C2 33 20 56 20 56 C20 56 38 33 38 20 C38 10 31 2 20 2 Z" fill="var(--gold-soft)"/>
        <circle cx="20" cy="20" r="7" fill="var(--poster-black)"/>
      </svg>
      <address style="font-style: normal;">
        Brindle9 Alehouse<br>
        413 Marlowe Ct #200,<br>
        Sacramento, CA 95821
      </address>
    </div>
    <div class="pricing">
      <svg width="110" height="90" viewBox="0 0 110 90" aria-hidden="true">
        <g transform="rotate(-22 55 45)" fill="none" stroke="var(--gold)" stroke-width="3">
          <rect x="14" y="36" width="84" height="34" rx="3"/>
          <rect x="10" y="24" width="88" height="36" rx="3" fill="var(--poster-black)"/>
          <rect x="16" y="30" width="76" height="24" rx="2" stroke-width="1.5"/>
          <text x="54" y="47" text-anchor="middle" font-family="Roboto, sans-serif" font-size="12" font-weight="500" fill="var(--gold)" stroke="none">TICKET</text>
        </g>
      </svg>
      <div class="pricing-label">GENERAL<br>SEATING</div>
      <div class="pricing-brace">}</div>
      <div class="pricing-values">$15 for adults<br>$10 for students</div>
    </div>
  </section>

  <div class="website">www.Tixolvo.com</div>
  <div class="website-rule"></div>
</main>
</body>
</html>
```